Business Card Design Project

"Crestline Record Services" is database management company working in the direct marketing & digital printing industries. Currently going through a name & rebranding process we require a new company business card.

Industry/Entity Type

Marketing

```html
<!DOCTYPE html>
<html lang="en">
<head>
<meta charset="utf-8">
<title>Crestline Record Services – Business Card</title>
<link rel="stylesheet" href="https://fonts.googleapis.com/css2?family=PT+Sans:wght@400;700&display=swap">
<style>
  :root {
    --backdrop: #e6e9ec;
    --card-white: #ffffff;
    --card-slate: #5c606b;
    --ink-slate: #4d515c;
    --ink-muted: #6a6e78;
    --accent-blue: #1f8fdc;
    --shadow: rgba(30, 40, 50, 0.18);
  }
  * { box-sizing: border-box; margin: 0; padding: 0; }
  html, body {
    width: 1200px;
    height: 960px;
    overflow: hidden;
    background: var(--backdrop);
    font-family: "PT Sans", Arial, sans-serif;
  }
  .canvas {
    position: relative;
    width: 1200px;
    height: 960px;
  }
  .card {
    position: absolute;
    left: 320px;
    width: 560px;
    height: 320px;
    border-radius: 4px;
    box-shadow: 0 10px 28px var(--shadow);
  }
  .card-front {
    top: 110px;
    background: var(--card-white);
  }
  .card-back {
    top: 520px;
    background: var(--card-slate);
    display: flex;
    align-items: center;
    justify-content: center;
  }

  /* Wordmark */
  .wordmark {
    font-weight: 700;
    line-height: 1.05;
    letter-spacing: 0.5px;
  }
  .card-front .wordmark {
    position: absolute;
    left: 44px;
    top: 70px;
    width: 220px;
    font-size: 30px;
    color: var(--ink-slate);
  }
  .card-back .wordmark {
    font-size: 34px;
    color: var(--card-white);
    text-align: center;
  }

  /* Contact block */
  .contact {
    position: absolute;
    left: 316px;
    top: 50px;
    width: 230px;
    color: var(--ink-muted);
  }
  .contact-name {
    font-size: 22px;
    color: var(--ink-slate);
  }
  .contact-role {
    font-size: 13px;
    margin-top: 2px;
  }
  .contact-lines {
    list-style: none;
    margin-top: 26px;
    font-size: 14px;
  }
  .contact-lines li {
    display: flex;
    align-items: center;
    gap: 8px;
    height: 21px;
  }
  .contact-icon {
    width: 13px;
    height: 13px;
    flex: none;
  }
  .contact-address {
    margin-top: 22px;
    font-size: 14px;
    line-height: 1.45;
  }
  .contact-web {
    font-weight: 700;
    color: var(--ink-slate);
  }
  .contact-web .accent { color: var(--accent-blue); }
</style>
</head>
<body>
<main class="canvas">

  <section class="card card-front" aria-label="Business card front">
    <div class="wordmark">Crestline Record Services</div>

    <div class="contact">
      <p class="contact-name">Renata Holloway</p>
      <p class="contact-role">Operation Manager</p>

      <ul class="contact-lines">
        <li>
          <svg class="contact-icon" viewBox="0 0 14 14" aria-hidden="true">
            <rect x="1" y="1" width="12" height="12" rx="1.5" fill="none" stroke="var(--accent-blue)" stroke-width="1.4"/>
            <rect x="3" y="3" width="3" height="8" fill="var(--accent-blue)"/>
            <rect x="8" y="3" width="3" height="2" fill="var(--accent-blue)"/>
            <rect x="8" y="6.5" width="3" height="1.5" fill="var(--accent-blue)"/>
            <rect x="8" y="9.5" width="3" height="1.5" fill="var(--accent-blue)"/>
          </svg>
          (221) 33 412 08 56
        </li>
        <li>
          <svg class="contact-icon" viewBox="0 0 14 14" aria-hidden="true">
            <rect x="3.5" y="0.8" width="7" height="12.4" rx="1.2" fill="none" stroke="var(--accent-blue)" stroke-width="1.4"/>
            <rect x="5" y="2.5" width="4" height="5" fill="var(--accent-blue)"/>
            <circle cx="7" cy="10.6" r="0.9" fill="var(--accent-blue)"/>
          </svg>
          (221) 77 501 64 83
        </li>
        <li>
          <svg class="contact-icon" viewBox="0 0 14 14" aria-hidden="true">
            <rect x="1" y="2.5" width="12" height="9" fill="none" stroke="var(--accent-blue)" stroke-width="1.4"/>
            <path d="M1 2.5 L7 8 L13 2.5 M1 11.5 L5.5 7 M13 11.5 L8.5 7" fill="none" stroke="var(--accent-blue)" stroke-width="1.2"/>
          </svg>
          name@crestlinerecords.com
        </li>
      </ul>

      <p class="contact-address">
        Rue des Tamariniers - Port Vert<br>
        BP 218 - City, Country<br>
        <span class="contact-web">www.crestline<span class="accent">records</span>.com</span>
      </p>
    </div>
  </section>

  <section class="card card-back" aria-label="Business card back">
    <div class="wordmark">Crestline<br>Record Services</div>
  </section>

</main>
</body>
</html>
```